Ridgeway Brew Label design/Graphic design

The Company
Ridgeway brew is an exciting new brand of ‘fit beer’ targeted at fitness enthusiasts as well as beer lovers. Ridgeway brew is a craft beer with added protein which can be used as a post work out recovery/leisure beverage. The target audience is generally male, 18-30 years old.
We need label/graphic design of the product to appear on our website www.ridgewaybrew.co.uk

The Project
The project is to submit four designs, one for each flavour:
• Larger
• Honey Ale
• Banana Ale
• Zero Alcohol

The design of each flavour must be differentiated, yet have a consistent theme throughout all flavours. At this point Ridgeway brew has no official logo so feel free to incorporate this into the design, although this is not absolutely necessary.

The label/design should include the following basic information:
Brand name: Ridgeway Brew
Type: Larger/Honey Ale/Banana Ale/Zero
Tag: 7g High Quality Protein
Alcohol percentage: 4%/Vol (0%/Vol for the Zero alcohol version)
Volume: 300ml

Brand Guidelines (designs not necessarily limited to these)
Font: Aldrich
Main Colours: Blue # 005fbf Orange # ed7000
Basic beer bottle image attached.

The final design will be displayed on (but not limited to) the website www.ridgewaybrew.co.uk

The winning designer may be contacted for future projects and opportunities with Ridgeway Brew.

Project Deadline Extended
Reason: My apologies I have been sick the last few days and have been unable to provide feedback. Your work is much appreciated, I will extend the project to give us a little more time and provide feedback individually later today. Best Regards, Oliver

Target Market(s)

The target audience is generally male, 18-30 years old.

Industry/Entity Type

Fitness

Requirements
Must have
• The label/design should include the following basic information:
Brand name: Ridgeway Brew
Volume: 300ml

```html
<!DOCTYPE html>
<html lang="en">
<head>
<meta charset="utf-8">
<title>Ridgeway Brew – Honey Ale Label</title>
<link rel="stylesheet" href="https://fonts.googleapis.com/css2?family=Cinzel:wght@500&family=Teko:wght@400;500;600&display=swap">
<style>
  :root {
    --label-black: #1f1b18;
    --ale-orange: #f29d1f;
    --ale-orange-deep: #e08a12;
    --ray-grey: #4a4642;
    --ink-white: #ffffff;
    --page: #ffffff;
  }
  html, body {
    margin: 0;
    padding: 0;
    width: 1200px;
    height: 848px;
    overflow: hidden;
    background: var(--page);
  }
  .canvas {
    position: relative;
    width: 1200px;
    height: 848px;
  }
  .label {
    position: absolute;
    left: 222px;
    top: 57px;
    width: 756px;
    height: 734px;
  }
  .serif { font-family: "Cinzel", Georgia, serif; font-weight: 500; }
  .condensed { font-family: "Teko", "Arial Narrow", sans-serif; }
  .txt-white { fill: var(--ink-white); }
  .txt-orange { fill: var(--ale-orange); }
</style>
</head>
<body>
<main class="canvas">
  <svg class="label" viewBox="0 0 540 524" xmlns="http://www.w3.org/2000/svg" aria-label="Ridgeway Brew Honey Ale label">
    <defs>
      <radialGradient id="rays" cx="50%" cy="100%" r="90%">
        <stop offset="0" stop-color="var(--ray-grey)"/>
        <stop offset="1" stop-color="var(--label-black)"/>
      </radialGradient>
      <clipPath id="oval-clip">
        <ellipse cx="272" cy="262" rx="193" ry="245"/>
      </clipPath>
      <path id="name-arc" d="M150 98 Q272 28 394 98"/>
    </defs>

    <!-- Label band -->
    <rect class="label-band" x="0" y="32" width="540" height="462" fill="var(--label-black)"/>

    <!-- Oval badge -->
    <ellipse class="badge-rim" cx="272" cy="262" rx="207" ry="259" fill="var(--label-black)" stroke="var(--ale-orange)" stroke-width="6"/>
    <ellipse class="badge-inner-rule" cx="272" cy="262" rx="193" ry="245" fill="none" stroke="var(--ink-white)" stroke-width="3"/>

    <!-- Upper arch with rays -->
    <g clip-path="url(#oval-clip)">
      <ellipse class="arch-rays" cx="272" cy="180" rx="128" ry="88" fill="url(#rays)" stroke="var(--ale-orange)" stroke-width="3" role="img" aria-label="Radiating sunburst rays behind the barbell"/>
      <rect class="arch-cut" x="60" y="180" width="430" height="200" fill="var(--label-black)"/>
      <ellipse class="arch-inner-rule" cx="272" cy="180" rx="116" ry="77" fill="none" stroke="var(--ink-white)" stroke-width="2.5"/>
      <rect class="arch-cut" x="60" y="181" width="430" height="200" fill="var(--label-black)"/>
      <line class="arch-base" x1="60" y1="180" x2="490" y2="180" stroke="var(--ink-white)" stroke-width="3"/>
      <!-- Lower curved rule -->
      <path class="base-curve" d="M80 422 Q272 390 464 422" fill="none" stroke="var(--ink-white)" stroke-width="3"/>
    </g>

    <!-- Flavour name -->
    <text class="serif txt-white" font-size="26" letter-spacing="3" text-anchor="middle">
      <textPath href="#name-arc" startOffset="50%">HONEY ALE</textPath>
    </text>

    <!-- Barbell emblem area -->
    <rect class="emblem-barbell" x="214" y="112" width="116" height="58" rx="4" fill="var(--ale-orange)" opacity="0.85" role="img" aria-label="Barbell emblem with scroll flourish"/>

    <!-- Side stars -->
    <rect class="side-star" x="88" y="205" width="26" height="26" fill="var(--ale-orange)" role="img" aria-label="Distressed star"/>
    <rect class="side-star" x="430" y="205" width="26" height="26" fill="var(--ale-orange)" role="img" aria-label="Distressed star"/>

    <!-- Brand name -->
    <text class="condensed txt-white" x="272" y="245" font-size="78" font-weight="500" text-anchor="middle" textLength="290" lengthAdjust="spacingAndGlyphs">RIDGEWAY</text>
    <text class="condensed txt-white" x="272" y="386" font-size="180" font-weight="600" text-anchor="middle" textLength="250" lengthAdjust="spacingAndGlyphs">BREW</text>

    <!-- Laurel sprigs -->
    <rect class="laurel" x="150" y="430" width="72" height="40" rx="6" fill="var(--ink-white)" opacity="0.9" role="img" aria-label="Left laurel sprig"/>
    <rect class="laurel" x="322" y="430" width="72" height="40" rx="6" fill="var(--ink-white)" opacity="0.9" role="img" aria-label="Right laurel sprig"/>

    <!-- Seal -->
    <circle class="seal" cx="272" cy="450" r="32" fill="var(--label-black)" stroke="var(--ale-orange)" stroke-width="4"/>

    <!-- Protein tag -->
    <text class="condensed txt-orange" font-size="26" font-weight="500" letter-spacing="1" transform="translate(14 42) rotate(90)">7G HIGH QUALITY PROTEIN</text>

    <!-- Alcohol -->
    <text class="condensed txt-orange" x="6" y="434" font-size="20" font-weight="500">ALC.</text>
    <text class="condensed txt-orange" x="38" y="456" font-size="66" font-weight="500">4%</text>
    <text class="condensed txt-orange" x="6" y="488" font-size="25" font-weight="500">BY VOLUME</text>

    <!-- Volume -->
    <text class="condensed txt-orange" x="444" y="455" font-size="20" font-weight="500">VOL.</text>
    <text class="condensed txt-orange" x="535" y="490" font-size="44" font-weight="500" text-anchor="end">300ML</text>
  </svg>
</main>
</body>
</html>
```